Cell Tower company needs website updated

We need a website that does not look like it was designed in the early 1990's. The company fabricates, installs and reinforces communication towers throughout the US, Caribbean, Central and S. America. We are located in Pensacola Florida. Our tower technicians travel to wherever the work is. I have some good pictures taken from towers to use on the site. I want the site to reflect the excitement that the wireless communication industry has. I want to the company to look exciting and attract new employees. The majority of our business is modifying and reinforcing existing cell towers to accept all the new tower top antennas that the increasing wireless mobile world demands.
Updates

I have added some sample photos from our business to our ArtBazaar profile.

We are now going through each design to find what is most suitable for our needs. Thank you all for your time in this matter.

Industry/Entity Type

Wireless Communication

```html
<!DOCTYPE html>
<html lang="en">
<head>
<meta charset="utf-8">
<title>TowerCraft — How We Do It</title>
<link href="https://fonts.googleapis.com/css2?family=PT+Sans:wght@400;700&display=swap" rel="stylesheet">
<style>
:root{
  --red:#c00000;
  --dark:#444444;
  --text:#555555;
  --muted:#8a8a8a;
  --line:#dddddd;
  --footer:#2f2f2f;
  --footer-bottom:#232323;
  --topbar-side:#333333;
  --white:#ffffff;
}
*{box-sizing:border-box;margin:0;padding:0}
html,body{width:694px;height:1200px;overflow:hidden;background:var(--white)}
body{position:relative;font-family:"PT Sans",Arial,sans-serif;color:var(--text)}
.abs{position:absolute}

/* top bar */
.topbar{left:0;top:0;width:694px;height:31px;background:var(--red)}
.topbar-search{left:571px;top:0;width:123px;height:31px;background:var(--topbar-side)}
.topbar-item{top:10px;font-size:7.5px;font-weight:700;color:var(--white);display:flex;align-items:center;gap:6px;white-space:nowrap}
.topbar-item .dot{width:8px;height:8px;border-radius:50%;background:var(--white);display:inline-block}

/* header */
.brand{left:83px;top:58px;display:flex;align-items:center;gap:6px}
.brand-mark{width:14px;height:14px;border-radius:50%;background:var(--red)}
.brand-name{font-size:24px;font-weight:700;color:var(--dark);letter-spacing:-0.5px}
.nav{right:82px;top:75px;display:flex;gap:12px;font-size:8.5px;font-weight:700;color:#555;white-space:nowrap}
.nav .active{color:var(--red)}

.page-title{left:75px;top:133px;font-size:16px;font-weight:700;color:var(--dark)}
.rule{height:1px;background:var(--line)}
.section-label{font-size:10.5px;font-weight:700;color:var(--dark);white-space:nowrap}

.hero{left:77px;top:223px;width:540px;height:204px;background:linear-gradient(100deg,#a07250 0%,#d3a877 30%,#ecd6a5 65%,#efe0b4 100%)}

.step-copy{left:224px;top:452px;width:345px;font-size:7.6px;line-height:11.5px;color:var(--muted);white-space:nowrap}

.step-title{font-size:10.5px;font-weight:700;color:var(--dark);white-space:nowrap}
.step-text{font-size:7.3px;line-height:11px;color:var(--muted);white-space:nowrap}

/* related */
.related-text{left:75px;top:894px;width:172px;font-size:7.3px;line-height:11.5px;color:var(--muted)}
.view-more{left:75px;top:938px;font-size:7.3px;color:var(--muted);display:flex;align-items:center;gap:10px}
.circle-btn{width:10px;height:10px;border-radius:50%;background:#bbb;display:inline-block;position:relative}
.circle-btn::after{content:"";position:absolute;left:3px;top:3px;width:3px;height:3px;border-top:1px solid #fff;border-right:1px solid #fff;transform:rotate(45deg)}
.circle-btn.light::after{border-color:#2f2f2f}
.thumb{top:868px;width:114px;height:70px}
.thumb-caption{top:948px;width:114px;text-align:center;font-size:7.3px;line-height:10.5px;color:var(--muted)}

/* footer */
.footer{left:0;top:1007px;width:694px;height:138px;background:var(--footer)}
.footer-bottom{left:0;top:1145px;width:694px;height:55px;background:var(--footer-bottom)}
.f-title{top:1040px;font-size:8.5px;font-weight:700;color:var(--white)}
.f-text{font-size:7px;line-height:11px;color:#cfcfcf}
.gallery-tile{width:46px;height:30px;background:linear-gradient(160deg,#6d8fb8,#b8c8da)}
.email-field{left:477px;top:1103px;width:87px;height:19px;background:#1c1c1c;color:var(--white);font-size:7px;line-height:19px;text-align:center}
.send-btn{left:564px;top:1103px;width:49px;height:19px;background:var(--red);color:var(--white);font-size:7px;line-height:19px;text-align:center}
.copyright{left:75px;top:1164px;font-size:7px;color:#cfcfcf}
.footer-links{left:253px;top:1164px;display:flex;gap:10px;font-size:7px;color:#cfcfcf}
.social{left:536px;top:1162px;display:flex;gap:6px}
.social span{width:11px;height:11px;border-radius:50%;background:#d8d8d8;display:block}
</style>
</head>
<body>

<div class="abs topbar"></div>
<div class="abs topbar-search">
  <svg class="abs" style="left:31px;top:10px" width="10" height="10" viewBox="0 0 10 10"><circle cx="5" cy="5" r="5" fill="#fff"/><circle cx="4.6" cy="4.6" r="1.8" fill="none" stroke="#333" stroke-width="1"/><line x1="5.9" y1="5.9" x2="7.3" y2="7.3" stroke="#333" stroke-width="1"/></svg>
</div>
<div class="abs topbar-item" style="left:83px"><span class="dot"></span>+800 555 0142 or 555 010 4477</div>
<div class="abs topbar-item" style="left:232px"><span class="dot"></span>hello@towercraft.test</div>
<div class="abs topbar-item" style="left:329px"><span class="dot"></span>live chat</div>

<header>
  <div class="abs brand"><span class="brand-mark"></span><span class="brand-name">TowerCraft</span></div>
  <nav class="abs nav">
    <span class="active">HOME</span><span>ABOUT US</span><span>SERVICES</span><span>BLOG</span><span>FAQS</span><span>CONTACT US</span>
  </nav>
</header>

<main>
  <h1 class="abs page-title">HOW WE DO IT</h1>
  <div class="abs rule" style="left:75px;top:166px;width:541px"></div>
  <h2 class="abs section-label" style="left:75px;top:191px">PROJECT PLANNING</h2>
  <div class="abs hero" role="img" aria-label="Photo of a satellite dish on a tower against a warm evening sky"></div>

  <svg class="abs" style="left:0;top:440px" width="694" height="380" viewBox="0 440 694 380">
    <g fill="none" stroke="#c8c8c8" stroke-width="1" stroke-dasharray="3 2">
      <line x1="147" y1="550" x2="147" y2="636"/>
      <line x1="147" y1="636" x2="328" y2="636"/>
      <line x1="375" y1="636" x2="414" y2="636"/>
      <line x1="288" y1="708" x2="328" y2="708"/>
      <line x1="375" y1="780" x2="414" y2="780"/>
    </g>
    <rect x="144" y="544" width="6" height="6" fill="#c8c8c8"/>
    <circle cx="147" cy="495" r="40" fill="var(--red)"/>
    <circle cx="147" cy="495" r="29" fill="#fff"/>
    <circle cx="147" cy="495" r="24" fill="#fff"/>
    <text x="147" y="507" text-anchor="middle" font-family="PT Sans, sans-serif" font-weight="700" font-size="32" fill="#c00000">1</text>
    <g font-family="PT Sans, sans-serif" font-weight="700" font-size="22" text-anchor="middle">
      <circle cx="351" cy="638" r="24" fill="var(--dark)"/><circle cx="351" cy="638" r="17" fill="#fff"/><text x="351" y="646" fill="#444">2</text>
      <circle cx="351" cy="710" r="24" fill="var(--dark)"/><circle cx="351" cy="710" r="17" fill="#fff"/><text x="351" y="718" fill="#444">3</text>
      <circle cx="351" cy="782" r="24" fill="var(--dark)"/><circle cx="351" cy="782" r="17" fill="#fff"/><text x="351" y="790" fill="#444">4</text>
    </g>
  </svg>

  <p class="abs step-copy">Lorem ipsum dolor sit amet voluptatem fugit aut illo omnis explicabo ipsa ipsa,<br>nemo rem ipsam quasi illo ut voluptatem doloremque perspiciatis beatae magni architecto<br>odit, aspernatur magni quae aperiam aut veritatis beatae eosvoluptas.<br>Doloremque perspiciatis error natus natus, qui aut eaque inventore aut quasi consequuntur<br>consequuntur ipsa aspernatur iste sit, quae explicabo dicta quasi. Doloremque perspiciatis<br>beatae magni architecto odit odit, aspernatur magni quae aperiam aut veritatis<br>beatae eos aut voluptas doloremque</p>

  <h3 class="abs step-title" style="right:148px;top:611px">PROJECT DESIGNING</h3>
  <p class="abs step-text" style="right:148px;top:633px;text-align:right">Voluptatem doloremque perspi beatae<br>ratione ratione dolores unde</p>

  <h3 class="abs step-title" style="left:149px;top:683px">PROJECT DEVELOPMENT</h3>
  <p class="abs step-text" style="left:149px;top:705px">Voluptatem doloremque perspi beatae<br>ratione ratione dolores unde</p>

  <h3 class="abs step-title" style="right:148px;top:755px">PROJECT PROMOTING</h3>
  <p class="abs step-text" style="right:148px;top:777px;text-align:right">Voluptatem doloremque perspi beatae<br>ratione ratione dolores unde</p>

  <div class="abs rule" style="left:75px;top:840px;width:543px"></div>

  <h2 class="abs section-label" style="left:77px;top:865px">OUR RELATED PROJECT</h2>
  <p class="abs related-text">Dolores voluptatem doloremque perspi beatae quia ratione ratione beatae quia ratione ratione dolores unde quas dolores unde quasi ratione</p>
  <div class="abs view-more">view more <span class="circle-btn"></span></div>

  <div class="abs thumb" style="left:265px;background:linear-gradient(170deg,#5c8fc9,#8db2d8 60%,#a6a6a6)" role="img" aria-label="Photo of a technician climbing a tower lattice"></div>
  <div class="abs thumb" style="left:386px;background:linear-gradient(170deg,#3f6fa6,#5a7fa8 50%,#6c5a4a)" role="img" aria-label="Photo of a worker welding steel on site"></div>
  <div class="abs thumb" style="left:507px;background:linear-gradient(170deg,#4a86c8,#86acd6 60%,#9aa3ad)" role="img" aria-label="Photo of a cell tower top with antennas"></div>
  <p class="abs thumb-caption" style="left:265px">Nemo rem ipsam quas illo<br>voluptatem explicabo</p>
  <p class="abs thumb-caption" style="left:386px">Nemo rem ipsam quas illo<br>voluptatem explicabo</p>
  <p class="abs thumb-caption" style="left:507px">Nemo rem ipsam quas illo<br>voluptatem explicabo</p>
</main>

<footer>
  <div class="abs footer"></div>
  <div class="abs footer-bottom"></div>

  <h4 class="abs f-title" style="left:75px">WHO WE ARE</h4>
  <p class="abs f-text" style="left:75px;top:1057px;width:105px">Fugit aut illo omnis explicabo ipsa, nemo rem ipsam quasi dolores voluptatem dolo perspiciatis beatae magni architecto odit</p>
  <div class="abs f-text" style="left:75px;top:1115px;display:flex;align-items:center;gap:7px;color:#fff">Read More <span class="circle-btn light" style="background:#ddd"></span></div>

  <h4 class="abs f-title" style="left:209px">ADDRESS</h4>
  <p class="abs f-text" style="left:209px;top:1057px">220 Harbor Lane Suite 12<br>Bayview FL 32500 - 0100<br>Hours M-F 8:00am-5:00pm<br>Fax. 555 010 2290</p>
  <div class="abs f-text" style="left:209px;top:1113px;display:flex;align-items:center;gap:6px">
    <svg width="6" height="9" viewBox="0 0 6 9"><path d="M3 0a3 3 0 0 1 3 3c0 2-3 6-3 6S0 5 0 3a3 3 0 0 1 3-3z" fill="#ddd"/><circle cx="3" cy="3" r="1" fill="#2f2f2f"/></svg>
    Open on the map</div>

  <h4 class="abs f-title" style="left:338px">GALLERY</h4>
  <span class="abs circle-btn light" style="left:427px;top:1041px;background:#ddd"></span>
  <div class="abs gallery-tile" style="left:338px;top:1056px" role="img" aria-label="Gallery photo of tower antennas"></div>
  <div class="abs gallery-tile" style="left:389px;top:1056px" role="img" aria-label="Gallery photo of tower antennas"></div>
  <div class="abs gallery-tile" style="left:338px;top:1091px" role="img" aria-label="Gallery photo of tower structure"></div>
  <div class="abs gallery-tile" style="left:389px;top:1091px" role="img" aria-label="Gallery photo of tower structure"></div>

  <h4 class="abs f-title" style="left:476px">CONTACT</h4>
  <p class="abs f-text" style="left:476px;top:1057px;width:148px">Nemo ipsam quasi dolores voluptatem dolo perspiciatis beatae magni architecto odit</p>
  <div class="abs email-field">enter your email</div>
  <div class="abs send-btn">send</div>

  <p class="abs copyright">© 2014 TowerCraft. All Rights Reserved.</p>
  <nav class="abs footer-links"><span>about us</span><span>term and use</span><span>privacy policy</span><span>career</span><span>contact us</span></nav>
  <div class="abs social" aria-label="Social links"><span></span><span></span><span></span><span></span><span></span></div>
</footer>

</body>
</html>
```